Top Service Company Billboard for busiest highway in County

Top Service company seeks a NEW design for Billboard across highest traffic road in Country - more than 500,000 cars per day.

RVK is a residential services company, providing our clients with, Cleaning, maintenance, Pest Control and AC Duct Cleaning.

Please see ATTACHED specifications -

3 Must HAVES
Envision the company photo being the center/core of the message -
RVK Cleaning
Prices starting at AED 25

Target Market(s)

Residential Home Owners & Renters

Industry/Entity Type

Residential

Font styles to use
Serif

Colors

Designer to choose colors to be used in the design.

Requirements
Must have
• This Billboard must be in half Arabic and English - please see attached specifications
• As well please check attached for height & width requirements.
• This billboard must really pop -
• Envision the company photo being the center/core of the message -
• RVK Cleaning
• Prices starting at AED 25
• Need a catch phrase...
Nice to have
• + RVK Pest Control + Bazar Mend Up Logo if possible
Should not have
• Should not be English only

```html
<!DOCTYPE html>
<html lang="en">
<head>
<meta charset="utf-8">
<title>RVK Cleaning Highway Billboard</title>
<link rel="stylesheet" href="https://fonts.googleapis.com/css2?family=Tinos:wght@400;700&family=Cairo:wght@700;800&display=swap">
<style>
  :root {
    --page-bg: #435d78;
    --navy: #2f3a66;
    --magenta: #d4379a;
    --orange: #f7941d;
    --slate: #47586f;
    --white: #ffffff;
    --brick: #b3262f;
    --blue: #2a6fc0;
    --photo-top: #c9d3dc;
    --photo-mid: #9a7f8a;
    --photo-low: #6b6f79;
  }
  * { margin: 0; padding: 0; box-sizing: border-box; }
  html, body {
    width: 1200px;
    height: 1200px;
    overflow: hidden;
    background: var(--page-bg);
  }
  .stage {
    width: 1200px;
    height: 1200px;
    display: flex;
    align-items: center;
    justify-content: center;
  }
  .billboard { width: 1046px; height: 80px; display: block; }
  .serif { font-family: "Tinos", "Times New Roman", serif; }
  .arabic { font-family: "Cairo", sans-serif; font-weight: 800; }
</style>
</head>
<body>
<main class="stage">
  <svg class="billboard" viewBox="0 0 1308 100" xmlns="http://www.w3.org/2000/svg" aria-label="RVK Cleaning bilingual billboard">
    <defs>
      <linearGradient id="team-photo" x1="0" y1="0" x2="0" y2="1">
        <stop offset="0" stop-color="var(--photo-top)"/>
        <stop offset="0.45" stop-color="var(--photo-mid)"/>
        <stop offset="1" stop-color="var(--photo-low)"/>
      </linearGradient>
      <linearGradient id="edge" x1="0" y1="0" x2="0" y2="1">
        <stop offset="0" stop-color="#1b2340"/>
        <stop offset="1" stop-color="#2c6bb5"/>
      </linearGradient>
    </defs>

    <rect class="board-base" x="0" y="0" width="1308" height="100" fill="var(--white)"/>

    <rect class="team-photo" x="480" y="0" width="348" height="100" fill="url(#team-photo)" role="img" aria-label="Company team photo with service vans"/>

    <g class="panel-english">
      <polygon class="headline-band" points="171,0 368,0 345,100 171,100 153,50" fill="var(--magenta)"/>
      <polygon class="accent-band" points="368,0 500,0 540,100 345,100" fill="var(--orange)"/>
      <polygon class="price-plate" points="366,14 498,14 486,56 378,56" fill="var(--slate)"/>
      <polygon class="partner-strip" points="372,61 505,61 543,100 345,100" fill="var(--white)"/>
    </g>

    <g class="panel-arabic" transform="translate(1308,0) scale(-1,1)">
      <polygon class="headline-band" points="171,0 368,0 345,100 171,100 153,50" fill="var(--magenta)"/>
      <polygon class="accent-band" points="368,0 500,0 540,100 345,100" fill="var(--orange)"/>
      <polygon class="price-plate" points="366,14 498,14 486,56 378,56" fill="var(--slate)"/>
      <polygon class="partner-strip" points="372,61 505,61 543,100 345,100" fill="var(--white)"/>
    </g>

    <rect class="edge-left" x="0" y="0" width="8" height="100" fill="url(#edge)"/>
    <rect class="edge-right" x="1300" y="0" width="8" height="100" fill="url(#edge)"/>

    <g class="brand-left serif" fill="var(--navy)">
      <circle cx="40" cy="50" r="15" fill="var(--magenta)"/>
      <text x="62" y="55" font-size="25">RVK</text>
      <text x="63" y="68" font-size="9" letter-spacing="0.8">CLEANING</text>
    </g>
    <g class="brand-right serif" fill="var(--navy)">
      <circle cx="1188" cy="50" r="15" fill="var(--magenta)"/>
      <text x="1210" y="55" font-size="25">RVK</text>
      <text x="1211" y="68" font-size="9" letter-spacing="0.8">CLEANING</text>
    </g>

    <g class="headline-english serif" fill="var(--white)" text-anchor="middle">
      <text x="265" y="33" font-size="17" font-weight="700">LOREM IPSUM</text>
      <text x="265" y="56" font-size="26">IS SIMPLY</text>
      <line x1="198" y1="60" x2="332" y2="60" stroke="var(--white)" stroke-width="1"/>
      <text x="265" y="76" font-size="16" letter-spacing="1.5">DUMMY TEXT</text>
      <line x1="198" y1="79" x2="332" y2="79" stroke="var(--white)" stroke-width="1"/>
    </g>

    <g class="price-english serif" text-anchor="middle">
      <text x="437" y="27" font-size="9" fill="var(--white)">PRICES STARTING</text>
      <text x="436" y="44" font-size="16" font-weight="700" fill="var(--orange)">AT AED 25</text>
    </g>

    <g class="price-arabic" text-anchor="middle">
      <text class="arabic" x="871" y="29" font-size="12" fill="var(--white)" direction="rtl">الأسعارتبدأ</text>
      <text class="serif" x="871" y="45" font-size="15" font-weight="700" fill="var(--orange)">25 AED من</text>
    </g>

    <g class="headline-arabic arabic" fill="var(--white)" text-anchor="middle" direction="rtl">
      <text x="1043" y="28" font-size="21">أبجدهوز</text>
      <text x="1043" y="52" font-size="21">هو مجرد</text>
      <line x1="978" y1="60" x2="1108" y2="60" stroke="var(--white)" stroke-width="1"/>
      <text x="1043" y="82" font-size="19">دمية النص</text>
      <line x1="978" y1="89" x2="1108" y2="89" stroke="var(--white)" stroke-width="1"/>
    </g>

    <g class="partners-left serif">
      <rect x="376" y="76" width="8" height="8" fill="var(--brick)"/>
      <text x="388" y="84" font-size="9" fill="var(--brick)">Bazar Mend Up</text>
      <text x="452" y="84" font-size="8" fill="var(--blue)">RVK Pest Control</text>
    </g>
    <g class="partners-right serif">
      <rect x="798" y="76" width="8" height="8" fill="var(--brick)"/>
      <text x="810" y="84" font-size="9" fill="var(--brick)">Bazar Mend Up</text>
      <text x="874" y="84" font-size="8" fill="var(--blue)">RVK Pest Control</text>
    </g>
  </svg>
</main>
</body>
</html>
```